FLYER FÜR KLARFRISCH HAMBURG
Zielgruppe
Zielgruppe ist zwischen 30 und 45 Jahre alt und berufstätig. Mit wenig Zeit für Einkauf und Zubereitung von Speisen, aber sehr gesundheitsbewusst und sportlich.
Aufgabenstellung
Ich bräuchte einen schnellen Flyer für Klarfrisch-Hamburg.com. Das Design sollte dem der Website entsprechen.
Ich habe auch eine Vorlage, die genommen werden kann, aber nicht muss.
Fotos und Texte liefere ich.
Der Flyer sollte Din hoch sein und zum aufklappen.
Ansonsten bin ich flexibel, sollte halt schön sein.
Preis inkl. MwSt, ich benötige eine Rechnung.

```html
<!DOCTYPE html>
<html lang="de">
<head>
<meta charset="utf-8">
<title>Klarfrisch Hamburg – Flyer</title>
<link rel="stylesheet" href="https://fonts.googleapis.com/css2?family=Oswald:wght@600;700&family=Noto+Sans:wght@400&display=swap">
<style>
  :root {
    --green: #248a3b;
    --green-dark: #1f7d34;
    --white: #ffffff;
    --ink: #1b1b1b;
  }
  * { margin: 0; padding: 0; box-sizing: border-box; }
  html, body { width: 1200px; height: 1200px; overflow: hidden; }
  body { background: var(--white); }

  .flyer {
    position: relative;
    width: 1200px;
    height: 1200px;
    background: var(--green);
    overflow: hidden;
  }

  .brand {
    position: absolute;
    left: 34px;
    top: 26px;
    font-family: "Oswald", "Arial Narrow", sans-serif;
    font-weight: 700;
    color: var(--white);
    line-height: 0.95;
    letter-spacing: 0.5px;
  }
  .brand-line-1 { display: block; font-size: 38px; }
  .brand-line-2 { display: block; font-size: 25px; letter-spacing: 2px; }

  .topic {
    position: absolute;
    left: 228px;
    width: 972px;
    height: 245px;
    background: var(--white);
  }
  .topic-1 { top: 115px; }
  .topic-2 { top: 379px; }
  .topic-3 { top: 641px; }
  .topic-4 { top: 906px; }

  .topic-photo {
    position: absolute;
    left: 12px;
    top: 12px;
    width: 331px;
    height: 222px;
  }
  .photo-jars   { background: linear-gradient(90deg, #f2a21c 0%, #e9e4d6 30%, #c9242a 60%, #efe9dc 85%, #f4f2ec 100%); }
  .photo-salad  { background: radial-gradient(ellipse at 50% 45%, #7fb34a 0%, #e98a4f 45%, #f2efe8 85%); }
  .photo-juices { background: linear-gradient(90deg, #f3f1ec 0%, #f0a21a 15%, #efece2 32%, #b8202c 50%, #d7c77a 68%, #ea6a1f 85%, #f3f1ec 100%); }
  .photo-smoothie { background: radial-gradient(ellipse at 45% 55%, #c8232e 0%, #5d8a2e 35%, #3f6d25 60%, #eef0ea 95%); }

  .topic-text {
    position: absolute;
    left: 399px;
    top: 16px;
    right: 20px;
  }
  .topic-title {
    font-family: "Oswald", "Arial Narrow", sans-serif;
    font-weight: 700;
    font-size: 31px;
    line-height: 1.1;
    color: var(--green-dark);
    margin-bottom: 2px;
  }
  .topic-body {
    font-family: "Noto Sans", Arial, sans-serif;
    font-size: 20.5px;
    line-height: 29px;
    color: var(--ink);
  }
</style>
</head>
<body>
<main class="flyer">
  <div class="brand">
    <span class="brand-line-1">KLARFRISCH</span>
    <span class="brand-line-2">HAMBURG</span>
  </div>

  <section class="topic topic-1">
    <div class="topic-photo photo-jars" role="img" aria-label="Foto: Gläser und Flaschen mit Säften, Müsli und Salaten"></div>
    <div class="topic-text">
      <h2 class="topic-title">WARUM DETOX?</h2>
      <p class="topic-body">Oximis nonduct urnium side aderist raedo, que<br>dentilicio, sentum idela consid mo iae<br>caequium re<br>novenihiliem revidit icpsene acestab ercestre<br>diis.<br>Duc fitiliactuus am nonfex ma, ussulis, uri castes</p>
    </div>
  </section>

  <section class="topic topic-2">
    <div class="topic-photo photo-salad" role="img" aria-label="Foto: frischer Salat mit Gemüse in einer Glasschale"></div>
    <div class="topic-text">
      <h2 class="topic-title">WARUM DETOX?</h2>
      <p class="topic-body">Oximis nonduct urnium side aderist raedo, que<br>dentilicio, sentum idela consid mo iae<br>caequium re<br>novenihiliem revidit icpsene acestab ercestre<br>diis.<br>Duc fitiliactuus am nonfex ma, ussulis, uri castes</p>
    </div>
  </section>

  <section class="topic topic-3">
    <div class="topic-photo photo-juices" role="img" aria-label="Foto: fünf Flaschen mit bunten Säften"></div>
    <div class="topic-text">
      <h2 class="topic-title">WARUM DETOX?</h2>
      <p class="topic-body">Oximis nonduct urnium side aderist raedo, que<br>dentilicio, sentum idela consid mo iae<br>caequium re<br>novenihiliem revidit icpsene acestab ercestre<br>diis.<br>Duc fitiliactuus am nonfex ma, ussulis, uri castes</p>
    </div>
  </section>

  <section class="topic topic-4">
    <div class="topic-photo photo-smoothie" role="img" aria-label="Foto: Mixbecher mit Obst, Kräutern und Johannisbeeren"></div>
    <div class="topic-text">
      <h2 class="topic-title">WARUM DETOX?</h2>
      <p class="topic-body">Oximis nonduct urnium side aderist raedo, que<br>dentilicio, sentum idela consid mo iae<br>caequium re<br>novenihiliem revidit icpsene acestab ercestre<br>diis.<br>Duc fitiliactuus am nonfex ma, ussulis, uri castes</p>
    </div>
  </section>
</main>
</body>
</html>
```